Marla Pettigrew Wordpress site

I want a word press website design for my current site. Current site can be found at www.velstromay.example and marlapettigrew.example VelstroMay is a consulting company that does strategic planning for start ups and emerging companies who are transitioning to their next level of growth. My target market includes start ups that are considering early stage and first round capital raises as well as municipalities looking for feasibility studies and/or financial opinions on large capital projects.My core business is around finance, budgeting, money and how to manage or obtain it.

My business is to create financial models for early stage businesses as well as provide risk analysis studies, feasibility studies, and strategic consulting. I also speak and write.

This means that I want my web presence to have a more corporate clean look as opposed to the more creative. Our industry colleagues would be commercial banks, Venture Capital firms, Consulting firms, Angel investor groups, and private equity firms.

I'd like to be able to add blogs and video to the site as well as keep the current content. Since I am also an author and I write books about fiance and business, I'd like to be able to sell books from the site. I'd also like to be able to capture email addresses or have potential client send me a question from the site.

I have included the company logo which was designed in Adobe Illustrator as well as personal photos included on the MarlaPettigrew site

Target Market(s)

Banks, municipalities, Venture capitalist, early stage start ups, entrepreneurs raising capital, angel investors, small businesses. consulting firms,private equity firms, radio stations, and television media

Number of Pages Required

2 page

Font styles to use
Sans Serif

Requirements
Must have
• Header, company logo, ability to load video, ability to load blogs, links to social media sites, ability to leave contact info or ask questions as well as a place where I can drop in items to sell like my e-book products.
• Please take a look at both sites: Velstromay.example and MarlaPettigrew.example I'm combining these two sites.
• Neutral colors--calming
Should not have
• Do not use the "simply Marla" logo. Don't have to use the simplymarla colors.

```html
<!DOCTYPE html>
<html lang="en">
<head>
<meta charset="utf-8">
<title>VelstroMay Associates</title>
<link href="https://fonts.googleapis.com/css2?family=Montserrat:wght@400;500;600;700&family=Open+Sans:ital,wght@0,400;0,600;0,700;1,400&display=swap" rel="stylesheet">
<style>
:root{
  --blue:#0b4694;
  --blue-bright:#1f6fd1;
  --red:#b3261e;
  --red-dark:#a9221b;
  --ink:#1e1e1e;
  --text:#444;
  --muted:#8a8a8a;
  --gray-bg:#ebebeb;
  --line:#dcdcdc;
  --white:#fff;
  --black:#0c0c0c;
}
*{box-sizing:border-box;margin:0;padding:0}
html,body{width:1200px;height:3571px;overflow:hidden}
body{font-family:"Open Sans",Arial,sans-serif;color:var(--text);background:var(--white);position:relative}
h1,h2,h3{font-weight:400}
a{color:inherit;text-decoration:none}

/* header */
.site-header{position:absolute;left:0;top:0;width:1200px;height:77px;background:var(--white)}
.brand{position:absolute;left:202px;top:22px;display:flex;align-items:center;gap:8px;font-family:"Montserrat",sans-serif;font-weight:700;font-size:24px;color:var(--blue)}
.brand-mark{width:14px;height:14px;background:var(--red)}
.main-nav{position:absolute;left:398px;top:29px;font-size:12px;color:var(--ink)}
.main-nav a{position:absolute;white-space:nowrap}
.search{position:absolute;left:738px;top:24px;width:167px;height:26px;border:1px solid #cfcfcf;border-radius:3px;font-size:11px;color:#aaa;padding:5px 10px}
.search svg{position:absolute;right:8px;top:6px}
.btn-contact{position:absolute;left:924px;top:24px;width:71px;height:26px;background:var(--blue);color:#fff;font-size:11px;font-weight:600;display:flex;align-items:center;justify-content:center;border-radius:2px}

/* hero */
.hero{position:absolute;left:0;top:77px;width:1200px;height:450px;background:linear-gradient(180deg,#1c2a44 0%,#3a3b4a 45%,#6a4a30 80%,#2a2420 100%);overflow:hidden}
.hero-photo{position:absolute;inset:0;background:radial-gradient(ellipse at 82% 60%,rgba(20,14,12,.85) 0 22%,transparent 40%)}
.hero h1{position:absolute;left:155px;top:136px;width:560px;font-family:"Montserrat",sans-serif;font-weight:500;font-size:33px;line-height:41px;color:#fff}
.hero p{position:absolute;left:160px;top:222px;width:500px;font-size:15px;line-height:20px;color:#fff}
.btn-hero{position:absolute;left:162px;top:299px;width:178px;height:48px;background:var(--blue-bright);color:#fff;font-family:"Montserrat",sans-serif;font-weight:600;font-size:14px;letter-spacing:.5px;display:flex;align-items:center;justify-content:center;border-radius:2px}

/* intro */
.intro{position:absolute;left:202px;top:618px;width:790px;font-size:11px;line-height:21px;color:#333}
.intro p{margin-bottom:14px}
.intro .points{color:var(--red);font-weight:700}
.intro .points span{margin-right:14px}
.rule-red{position:absolute;left:0;top:823px;width:1200px;height:2px;background:#e4a09a}

/* blog */
.blog{position:absolute;left:0;top:825px;width:1200px;height:648px;background:var(--gray-bg)}
.section-title{position:absolute;left:202px;top:50px;font-family:"Montserrat",sans-serif;font-weight:400;font-size:23px;letter-spacing:1px;color:var(--ink)}
.section-title em{font-style:normal;color:var(--red)}
.blog-card{position:absolute;left:231px;top:114px;width:769px;height:421px;background:#fff;box-shadow:0 1px 3px rgba(0,0,0,.08)}
.post{position:absolute;left:19px;width:705px;height:110px;border-bottom:1px solid var(--line)}
.post-thumb{position:absolute;left:0;top:10px;width:160px;height:90px;background:linear-gradient(135deg,#b7c6d6,#e7ebef 60%,#9aa7b4)}
.post h3{position:absolute;left:186px;top:10px;font-family:"Montserrat",sans-serif;font-weight:500;font-size:17px;color:var(--ink)}
.post p{position:absolute;left:186px;top:38px;width:480px;font-size:9px;line-height:13px;color:var(--muted)}
.post .more{position:absolute;left:186px;top:82px;font-size:9px;font-weight:700;color:var(--blue)}
.post .icons{position:absolute;left:617px;top:14px;display:flex;gap:18px}
.scroll-track{position:absolute;left:738px;top:42px;width:12px;height:350px;background:#eee}
.scroll-thumb{position:absolute;left:738px;top:42px;width:12px;height:90px;background:#c4c4c4}
.btn-visit{position:absolute;left:202px;top:574px;width:91px;height:31px;background:#b5b5b5;color:#fff;font-size:9px;font-weight:700;display:flex;align-items:center;justify-content:center}

/* video */
.video{position:absolute;left:0;top:1473px;width:1200px;height:534px;background:linear-gradient(180deg,#8c8c8c 0%,#5a5a5a 55%,#2e2e2e 100%)}
.play{position:absolute;left:560px;top:225px;width:80px;height:64px;background:#fff;border-radius:14px}
.play svg{position:absolute;left:28px;top:18px}

/* features band */
.features{position:absolute;left:0;top:2007px;width:1200px;height:213px;background:var(--blue);color:#fff}
.feature{position:absolute;top:50px;width:380px}
.feature h2{font-family:"Montserrat",sans-serif;font-weight:500;font-size:21px;margin-bottom:10px}
.feature p{font-size:11.5px;line-height:16px;font-weight:600}

/* ebook */
.ebook-cover{position:absolute;left:250px;top:2330px;width:321px;height:264px;background:linear-gradient(160deg,#2b3e4a,#4a6470);border-radius:14px 14px 0 0;border:8px solid #111;border-bottom:none}
.ebook-title{position:absolute;left:626px;top:2338px;font-family:"Montserrat",sans-serif;font-weight:400;font-size:35px;color:var(--ink)}
.ebook-title em{font-style:normal;color:var(--red)}
.ebook-text{position:absolute;left:626px;top:2392px;width:320px;font-size:15px;line-height:19px;color:#333}
.btn-download{position:absolute;left:626px;top:2462px;width:148px;height:36px;background:var(--blue);color:#fff;font-size:12px;font-weight:600;display:flex;align-items:center;justify-content:center}
.ebook-prev{position:absolute;left:626px;top:2516px;font-size:13px;color:#555;text-decoration:underline}

/* cta band */
.cta-band{position:absolute;left:0;top:2594px;width:1200px;height:113px;background:var(--gray-bg)}
.cta-band p{position:absolute;left:236px;top:46px;width:520px;font-size:15px;line-height:20px;color:#333;white-space:nowrap}
.btn-cta{position:absolute;left:788px;top:33px;width:181px;height:46px;background:var(--red);color:#fff;font-family:"Montserrat",sans-serif;font-weight:600;font-size:14px;display:flex;align-items:center;justify-content:center;border:1px solid #7e1812}

/* review */
.review h2{position:absolute;left:0;top:2750px;width:1200px;text-align:center;font-family:"Montserrat",sans-serif;font-weight:400;font-size:27px;color:var(--ink)}
.review blockquote{position:absolute;left:300px;top:2830px;width:600px;text-align:center;font-style:italic;font-size:13px;line-height:20px;color:#777}
.review cite{position:absolute;left:0;top:2891px;width:1200px;text-align:center;font-style:normal;font-weight:700;font-size:12px;color:#222}
.carousel{position:absolute;left:512px;top:2924px}

/* contact */
.contact{position:absolute;left:0;top:3046px;width:1200px;height:374px;background:var(--red-dark)}
.contact h2{position:absolute;left:0;top:30px;width:1200px;text-align:center;font-family:"Montserrat",sans-serif;font-weight:500;font-size:18px;letter-spacing:1.5px;color:#fff}
.field{position:absolute;background:#fff;border-radius:3px;font-style:italic;font-size:14px;color:#999;padding:14px 22px}
.btn-submit{position:absolute;left:336px;top:281px;width:528px;height:50px;background:var(--black);color:#fff;font-family:"Montserrat",sans-serif;font-weight:700;font-size:14px;letter-spacing:1px;display:flex;align-items:center;justify-content:center}

/* footer */
.footer-nav{position:absolute;left:202px;top:3465px;font-size:12px;color:#333}
.footer-nav a{margin-right:28px}
.footer-rule{position:absolute;left:202px;top:3491px;width:496px;height:1px;background:#cfcfcf}
.social{position:absolute;left:205px;top:3505px;display:flex;gap:11px}
.social span{width:25px;height:25px;border-radius:50%}
.copyright{position:absolute;left:202px;top:3546px;font-size:9px;color:#888}
.btn-newsletter{position:absolute;left:833px;top:3475px;width:162px;height:22px;background:#444;color:#fff;font-size:9px;font-weight:700;display:flex;align-items:center;justify-content:center}
</style>
</head>
<body>

<header class="site-header">
  <a class="brand" href="#"><span class="brand-mark"></span>VelstroMay</a>
  <nav class="main-nav">
    <a style="left:0">Home</a>
    <a style="left:54px">What we do</a>
    <a style="left:147px">Clients</a>
    <a style="left:212px">Vision</a>
    <a style="left:274px">News</a>
  </nav>
  <div class="search">Search VelstroMay
    <svg width="12" height="12" viewBox="0 0 12 12"><circle cx="5" cy="5" r="3.8" fill="none" stroke="#333" stroke-width="1.5"/><line x1="8" y1="8" x2="11" y2="11" stroke="#333" stroke-width="1.6"/></svg>
  </div>
  <a class="btn-contact" href="#">Contact Us</a>
</header>

<section class="hero">
  <div class="hero-photo" role="img" aria-label="Night city skyline with a smiling consultant in a dark suit"></div>
  <h1>Strategic planning for start ups &amp; emerging companies</h1>
  <p>To create financial models for early stage businesses as well as provide risk analysis studies, feasibility studies, and strategic consulting.</p>
  <a class="btn-hero" href="#">CALL TO ACTION</a>
</section>

<section class="intro">
  <p>Velstro May Associates, LLC is a consulting firm that assists emerging and startup companies in improving their business and financial strategies. Our services and solutions address organizational issues that impact a company's ability to:<br>
  <span class="points"><span>• Improve overall business strategy and planning</span><span>• Affect leadership development</span><span>• Raise capital funds</span></span></p>
  <p>At Velstro May Associates, LLC, we believe that strong leadership and consistent strategic planning is the key to moving emerging companies into legacy position. We help develop leaders and their companies by challenging them to become better, better informed, better prepared, and better disciplined.</p>
  <p>Whether we are helping business leaders prepare to raise funds for their organization, or assisting them in preparing a strategic startup plan, we help them focus on three critical basic business components: Strategy, Finance and Leadership. We bring objectivity to the strategic plan, consistency and structure to the financial plan and ultimately strength to the leadership team.</p>
</section>
<div class="rule-red"></div>

<section class="blog">
  <h2 class="section-title">FROM THE <em>BLOG</em></h2>
  <div class="blog-card">
    <article class="post" style="top:14px">
      <div class="post-thumb" role="img" aria-label="Business meeting photo"></div>
      <h3>Lorem ipsum dolor ready</h3>
      <p>Lorem ipsum dolor sit amet, consectetur adipisicing elit, sed do eiusmod tempor incididunt ut labore et dolore magna aliqua. Ut enim ad minim veniam, quis nostrud exercitation ullamco laboris nisi ut aliquip ex ea commodo consequat. Duis aute irure dolor in reprehenderit.</p>
      <a class="more">READ POST</a>
      <div class="icons">
        <svg width="13" height="13" viewBox="0 0 13 13"><circle cx="10" cy="2.5" r="2" fill="#222"/><circle cx="3" cy="6.5" r="2" fill="#222"/><circle cx="10" cy="10.5" r="2" fill="#222"/><path d="M10 2.5L3 6.5L10 10.5" stroke="#222" fill="none"/></svg>
        <svg width="15" height="11" viewBox="0 0 15 11"><rect width="15" height="11" fill="#222"/><path d="M0 0L7.5 6L15 0" stroke="#fff" fill="none"/></svg>
      </div>
    </article>
    <article class="post" style="top:141px">
      <div class="post-thumb" role="img" aria-label="Business meeting photo"></div>
      <h3>Lorem ipsum dolor ready</h3>
      <p>Lorem ipsum dolor sit amet, consectetur adipisicing elit, sed do eiusmod tempor incididunt ut labore et dolore magna aliqua. Ut enim ad minim veniam, quis nostrud exercitation ullamco laboris nisi ut aliquip ex ea commodo consequat. Duis aute irure dolor in reprehenderit.</p>
      <a class="more">READ POST</a>
      <div class="icons">
        <svg width="13" height="13" viewBox="0 0 13 13"><circle cx="10" cy="2.5" r="2" fill="#222"/><circle cx="3" cy="6.5" r="2" fill="#222"/><circle cx="10" cy="10.5" r="2" fill="#222"/><path d="M10 2.5L3 6.5L10 10.5" stroke="#222" fill="none"/></svg>
        <svg width="15" height="11" viewBox="0 0 15 11"><rect width="15" height="11" fill="#222"/><path d="M0 0L7.5 6L15 0" stroke="#fff" fill="none"/></svg>
      </div>
    </article>
    <article class="post" style="top:268px;border-bottom:none">
      <div class="post-thumb" role="img" aria-label="Business meeting photo"></div>
      <h3>Lorem ipsum dolor ready</h3>
      <p>Lorem ipsum dolor sit amet, consectetur adipisicing elit, sed do eiusmod tempor incididunt ut labore et dolore magna aliqua. Ut enim ad minim veniam, quis nostrud exercitation ullamco laboris nisi ut aliquip ex ea commodo consequat. Duis aute irure dolor in reprehenderit.</p>
      <a class="more">READ POST</a>
      <div class="icons">
        <svg width="13" height="13" viewBox="0 0 13 13"><circle cx="10" cy="2.5" r="2" fill="#222"/><circle cx="3" cy="6.5" r="2" fill="#222"/><circle cx="10" cy="10.5" r="2" fill="#222"/><path d="M10 2.5L3 6.5L10 10.5" stroke="#222" fill="none"/></svg>
        <svg width="15" height="11" viewBox="0 0 15 11"><rect width="15" height="11" fill="#222"/><path d="M0 0L7.5 6L15 0" stroke="#fff" fill="none"/></svg>
      </div>
    </article>
    <div class="scroll-track"></div>
    <div class="scroll-thumb"></div>
  </div>
  <a class="btn-visit" href="#">VISIT BLOG</a>
</section>

<section class="video" role="img" aria-label="Video still of a speaker presenting a chart to a seated audience">
  <div class="play">
    <svg width="26" height="28" viewBox="0 0 26 28"><path d="M2 1L25 14L2 27Z" fill="#111"/></svg>
  </div>
</section>

<section class="features">
  <div class="feature" style="left:193px">
    <h2>Lorem ipsum dolor</h2>
    <p>Lorem ipsum dolor sit amet, consectetur adipiscing elit, sed do eiusmod tempor incididunt ut labore et dolore magna aliqua. Ut enim ad minim veniam, quis nostrud exercitation ullamco laboris nisi ut aliquip ex ea commodo consequat.</p>
  </div>
  <div class="feature" style="left:614px">
    <h2>Vasatn editm hexam</h2>
    <p>Duis aute irure dolor in reprehenderit in voluptate velit esse cillum dolore eu fugiat nulla pariatur. Excepteur sint occaecat cupidatat non proident, sunt in culpa qui officia deserunt mollit anim id est laborum, pariatur. Excepteur sint occaecat cupidatat.</p>
  </div>
</section>

<section class="ebook">
  <div class="ebook-cover" role="img" aria-label="Tablet showing an eBook cover on business process management"></div>
  <h2 class="ebook-title"><em>May's</em> free eBook</h2>
  <p class="ebook-text">Lorem ipsum dolor sit amet, consectetur adipiscing elit, sed do eiusmod tempor incididunt ut labore.</p>
  <a class="btn-download" href="#">DOWNLOAD NOW</a>
  <a class="ebook-prev" href="#">Download previous issues</a>
</section>

<section class="cta-band">
  <p>Sed ut perspiciatis unde omnis iste natus error sit voluptatem.</p>
  <a class="btn-cta" href="#">CALL TO ACTION</a>
</section>

<section class="review">
  <h2>Client review</h2>
  <blockquote>"Lorem ipsum dolor sit amet, consectetur adipisicing elit, sed do eiusmod tempor incididunt ut labore et dolore magna aliqua. Ut enim ad minim veniam, quis nostrud exercitation ullamco laboris nisi ut aliquip ex ea commodo consequat. Duis aute irure dolor in reprehenderit in."</blockquote>
  <cite>JOHN DOE</cite>
  <svg class="carousel" width="176" height="30" viewBox="0 0 176 30">
    <circle cx="14" cy="15" r="12" fill="none" stroke="#222" stroke-width="1.5"/>
    <path d="M17 9L11 15L17 21" fill="none" stroke="#222" stroke-width="2"/>
    <circle cx="55" cy="15" r="6" fill="#111"/>
    <circle cx="75" cy="15" r="6" fill="#d0d0d0"/>
    <circle cx="95" cy="15" r="6" fill="#d0d0d0"/>
    <circle cx="115" cy="15" r="6" fill="#d0d0d0"/>
    <circle cx="162" cy="15" r="12" fill="none" stroke="#222" stroke-width="1.5"/>
    <path d="M159 9L165 15L159 21" fill="none" stroke="#222" stroke-width="2"/>
  </svg>
</section>

<section class="contact">
  <h2>FOR ANY QUERY OR QUESTIONS, CONTACT US</h2>
  <div class="field" style="left:336px;top:91px;width:257px;height:51px">Full name*</div>
  <div class="field" style="left:607px;top:91px;width:257px;height:51px">Email address*</div>
  <div class="field" style="left:336px;top:156px;width:528px;height:110px">Your message*</div>
  <a class="btn-submit" href="#">SUBMIT</a>
</section>

<footer>
  <nav class="footer-nav"><a>Home</a><a>What we do</a><a>Clients</a><a>Vision</a><a>News</a></nav>
  <div class="footer-rule"></div>
  <div class="social">
    <span style="background:#3b5ba8"></span>
    <span style="background:#f0952a"></span>
    <span style="background:#3fa9e6"></span>
    <span style="background:#d6302a"></span>
  </div>
  <p class="copyright">©2016 All rights reserved</p>
  <a class="btn-newsletter" href="#">JOIN NEWSLETTER</a>
</footer>

</body>
</html>
```